TimeLatticeo One Page Flier

Create an editable, professional one-sided, one page flier in either a word doc or a power point slide, that summarizes what TimeLatticeo can do for the purpose of selling this product to acquisitive companies in tech, pharma, finance, consulting. I have attached a summary of topics to include, hoping to cover all ten topics listed below in one page if possible.
1) Headline and value proposition
2) Why TimeLatticeo matters for M&A
3) What TimeLatticeo does
4) Typical M&A use cases
5) ROI / Outcomes
6) Notable customer logos
7) Security and Compliance
8) How it works - simple diagram (Company A Calendar <--> TimeLatticeo Sync Engine <--> Company B Calendar)
9) Deployment Model
10) Call to Action

I have attached a couple versions of our current one page content, along with the TimeLatticeo logo.
we'd like the colors to be consistent with our website. Please reference the website for branding and additional content: https://www.timelatticeo.example

About TimeLatticeo
TimeLatticeo helps professionals, teams, and organizations manage their multiple calendars seamlessly and with confidence. We provide:
• Real-time calendar sync — when you update an event on one calendar, it propagates to your other Vantora Mail, Glimmer, and iCloud calendars, so your availability is consistent across all.
• Unified Calendar interface — view, edit, and manage Glimmer, Vantora Mail, iCloud, and ICS calendars in one streamlined dashboard.
• AI Scheduling Assistant — just CC our assistant in an email; it reads your availability across synced calendars and proposes meeting times right inside the conversation.
• Smart scheduling pages — you can share links that reflect combined availability across all your calendars, making booking simple and accurate.

Our Mission & Value Proposition
In a world where people juggle multiple calendars across work, personal, and side projects, conflict, fatigue, and wasted time are common. TimeLatticeo empowers users to eliminate “double bookings,” reduce back-and-forth scheduling email chains, and regain control of their time—all while preserving privacy and data integrity.

We never store, analyze, or sell your calendar data. Through secure OAuth2 connections, we only request the minimal permissions needed. You control what syncs, when, and how.

Who We Serve

• Consultants, freelancers, and solopreneurs managing many calendar accounts
• Fractional and part-time professionals with split schedules
• Teams and organizations seeking centralized scheduling and sync
• Users who want work-life balance by keeping personal and professional calendars aligned

Target Market(s)

Corporate Development Leaders, Integration Leaders, IMO Leaders, HR, Finance, Legal

Industry/Entity Type

Financial Services, Consulting Firms, Pharmaceutical

Font styles to use
Sans Serif
Other font styles liked:
• Helvetica

Colors
0054AA
0677BA
7BADD7
CADEEF
E8F1F8
EE7325
F08F49
F5BC92
FAE3D3
FDF4ED

Requirements
Must have
• one page, one-sided, professional flier on a word document
Should not have
• more than one page

```html
<!DOCTYPE html>
<html lang="en">
<head>
<meta charset="utf-8">
<title>TimeLatticeo – Seamless Day-1 Collaboration for Modern M&amp;A</title>
<link rel="stylesheet" href="https://fonts.googleapis.com/css2?family=Inter:wght@400;500;600;700;800&display=swap">
<style>
  :root{
    --page-bg:#1a5fa8;
    --blue-900:#0054AA;
    --blue-700:#0677BA;
    --blue-400:#7BADD7;
    --blue-200:#CADEEF;
    --blue-100:#E8F1F8;
    --orange-600:#EE7325;
    --orange-500:#F08F49;
    --orange-300:#F5BC92;
    --orange-100:#FAE3D3;
    --orange-50:#FDF4ED;
    --text:#2f3338;
    --logo-text:#4a5563;
    --panel:#f4f4f8;
    --white:#ffffff;
  }
  *{box-sizing:border-box;margin:0;padding:0}
  html,body{width:918px;height:1200px;overflow:hidden}
  body{background:var(--page-bg);font-family:"Inter",Helvetica,Arial,sans-serif;color:var(--text);position:relative}

  .flier{position:absolute;left:97px;top:87px;width:724px;height:1025px;background:var(--white);overflow:hidden}

  /* Header */
  .hero{position:absolute;left:0;top:0;width:724px;height:228px;
    background:
      radial-gradient(ellipse 260px 160px at 100% 0%, rgba(253,244,237,.95), rgba(253,244,237,0) 70%),
      linear-gradient(90deg,#8fcdf7 0%,#2f82c0 30%,#3f7fb3 50%,#8b99aa 70%,#c99a80 85%,#e7752f 100%);
    text-align:center;color:var(--white)}
  .brand{position:absolute;top:20px;left:0;right:0;display:flex;justify-content:center;align-items:center;gap:10px}
  .brand-mark{width:20px;height:20px;background:var(--orange-500);border-radius:3px}
  .brand-name{font-size:25px;font-weight:500;letter-spacing:-.2px}
  .hero-title{position:absolute;top:82px;left:0;right:0;font-size:29.5px;font-weight:800;line-height:31px;letter-spacing:-.2px;text-transform:uppercase}
  .hero-lede{position:absolute;top:149px;left:80px;width:564px;font-size:12px;line-height:17px;font-weight:400}

  /* Columns */
  .col-right{position:absolute;left:338px;top:228px;width:386px;height:814px;background:var(--panel)}
  .section{position:absolute}
  .section h2{font-size:14.8px;font-weight:700;color:var(--blue-900);letter-spacing:-.1px;margin-bottom:6px}
  .checklist{list-style:none}
  .checklist li{position:relative;padding-left:23px;font-size:11px;line-height:13.4px;margin-bottom:6.5px}
  .checklist li::before{content:"";position:absolute;left:0;top:0;width:12px;height:12px;border:1.1px solid var(--orange-600);border-radius:50%}
  .checklist li::after{content:"";position:absolute;left:4px;top:2.6px;width:3.2px;height:5.4px;border:solid var(--orange-600);border-width:0 1.2px 1.2px 0;transform:rotate(45deg)}
  .checklist.roomy li{padding-left:18px;line-height:14.5px;margin-bottom:8.5px;font-size:11.2px}

  /* Customer names */
  .logo-grid{position:relative;width:290px;height:110px}
  .logo-name{position:absolute;font-weight:700;color:var(--logo-text);white-space:nowrap;font-size:12.5px}

  /* ROI */
  .roi h2{color:var(--orange-600);font-size:16.5px;margin-bottom:10px}
  .roi-list{list-style:none}
  .roi-list li{position:relative;width:264px;background:var(--white);box-shadow:0 1px 2px rgba(0,40,90,.12);color:var(--blue-700);font-size:11px;line-height:14.5px;padding:5.5px 10px 5.5px 24px;margin-bottom:8.5px}
  .roi-list li::before{content:"";position:absolute;left:9px;top:9.5px;border-left:5px solid var(--orange-600);border-top:4px solid transparent;border-bottom:4px solid transparent}

  /* How it works */
  .how{position:absolute;left:338px;top:692px;width:386px;height:90px;background:var(--blue-900)}
  .how h2{position:absolute;left:22px;top:14px;color:var(--white);font-size:17px;font-weight:700}
  .flow{position:absolute;left:0;top:0;width:386px;height:90px}
  .flow-node{position:absolute;top:43px;height:32px;background:var(--white);color:var(--blue-900);font-size:10.5px;font-weight:700;line-height:12.5px;padding:3.5px 7px;text-transform:uppercase;white-space:nowrap}

  /* Footer */
  .cta-band{position:absolute;left:0;top:955px;width:724px;height:70px;
    background:linear-gradient(90deg,#8ecdf7 0%,#2b7ebd 30%,#5f93bb 50%,#b7c0c8 72%,#f2c4a6 90%,#f0b690 100%)}
  .cta-button{position:absolute;left:243px;top:22px;width:238px;height:30px;background:var(--white);color:var(--orange-600);font-size:14.5px;font-weight:700;text-align:center;line-height:30px;letter-spacing:.1px}
</style>
</head>
<body>
<main class="flier">

  <header class="hero">
    <div class="brand">
      <span class="brand-mark"></span>
      <span class="brand-name">timelatticeo</span>
    </div>
    <h1 class="hero-title">Seamless Day-1<br>Collaboration for Modern M&amp;A</h1>
    <p class="hero-lede">When companies join through acquisition, calendars, tenants, and collaboration tools often remain disconnected for weeks or months. TimeLatticeo enables newly combined teams to see availability and schedule immediately-without requiring IT migrations or workflow disruption.</p>
  </header>

  <div class="col-right"></div>

  <!-- Left column -->
  <section class="section" style="left:40px;top:250px;width:290px">
    <h2>Why TimeLatticeo Matters for M&amp;A</h2>
    <ul class="checklist">
      <li>Integration leaders, IMO, HR, Finance, Legal, &amp; Product teams must coordinate immediately.</li>
      <li>Without shared calendar visibility, teams rely on email ping-pong and manual workarounds.</li>
      <li>Day-1 migrations (Glimmer → Vantora or vice-versa) create unnecessary disruption.</li>
      <li>TimeLatticeo enables collaboration to start instantly, while IT integrates systems later.</li>
    </ul>
  </section>

  <section class="section" style="left:40px;top:420px;width:296px">
    <h2>What TimeLatticeo does</h2>
    <ul class="checklist">
      <li>Real-time cross-tenant calendar syncing (Vantora → Vantora, Glimmer → Glimmer, Glimmer → Vantora)</li>
      <li>Availability shows natively inside Vantora Mail Scheduling Assistant and Glimmer Calendar</li>
      <li>Zero-password, OAuth2-only, minimal permissions</li>
      <li>Busy-only, limited-details, or full-details sync</li>
      <li>Deploys in minutes-no domain merge<br>or tenant migration needed</li>
    </ul>
  </section>

  <section class="section" style="left:40px;top:608px;width:290px">
    <h2>Typical M&amp;A use cases</h2>
    <ul class="checklist">
      <li>Perpetually Coexisting Tenants<br>(parent + subsidiaries)</li>
      <li>Temporary Coexistence: Day-1 M&amp;A,<br>JVs, consulting, outsourced teams</li>
      <li>AI Assistant-Ready Scheduling without<br>exposing event details</li>
      <li>Unified Virtual Calendar Layer without<br>actual tenant consolidation</li>
    </ul>
  </section>

  <section class="section" style="left:41px;top:786px;width:290px">
    <h2>We Are Trusted by Major Companies</h2>
    <div class="logo-grid" aria-label="Customer names">
      <span class="logo-name" style="left:0;top:10px">Harborline</span>
      <span class="logo-name" style="left:92px;top:10px">Quillvane</span>
      <span class="logo-name" style="left:180px;top:10px">Stratacore</span>
      <span class="logo-name" style="left:0;top:44px">Meridane</span>
      <span class="logo-name" style="left:100px;top:44px">Calloway</span>
      <span class="logo-name" style="left:196px;top:44px">Brightfold</span>
      <span class="logo-name" style="left:0;top:80px">Nethaven</span>
      <span class="logo-name" style="left:68px;top:80px">Veltris Pharma</span>
      <span class="logo-name" style="left:170px;top:80px">Crestmoor</span>
      <span class="logo-name" style="left:244px;top:80px">Rydelo</span>
    </div>
  </section>

  <!-- Right column -->
  <section class="section" style="left:362px;top:250px;width:340px">
    <h2>Security and Compliance</h2>
    <ul class="checklist roomy">
      <li>Zero-password system (OAuth2-only)</li>
      <li>Minimal permissions (no email, file,<br>or contact access)</li>
      <li>Privacy-safe calendar sharing</li>
      <li>Works safely for regulated and<br>ring-fenced environments</li>
    </ul>
  </section>

  <section class="section roi" style="left:362px;top:413px;width:300px">
    <h2>ROI / Outcomes</h2>
    <ul class="roi-list">
      <li>True Day-1 operational readiness</li>
      <li>Cuts weeks off post-acquisition<br>collaboration ramp-up</li>
      <li>Eliminates meeting-coordination delays</li>
      <li>Reduces scheduling bottlenecks for<br>integration teams</li>
      <li>Avoids unnecessary IT migrations</li>
      <li>Improves acquired employee experience</li>
    </ul>
  </section>

  <section class="how">
    <h2>How it works</h2>
    <svg class="flow" viewBox="0 0 386 90" aria-hidden="true">
      <line x1="106" y1="59" x2="128" y2="59" stroke="#7BADD7" stroke-width="1"/>
      <line x1="239" y1="59" x2="261" y2="59" stroke="#7BADD7" stroke-width="1"/>
    </svg>
    <div class="flow-node" style="left:22px;width:84px">Company A<br>Calendar</div>
    <div class="flow-node" style="left:128px;width:111px">TimeLatticeo<br>Sync Engine</div>
    <div class="flow-node" style="left:261px;width:84px">Company B<br>Calendar</div>
  </section>

  <section class="section" style="left:362px;top:807px;width:340px">
    <h2>Deployment Model</h2>
    <ul class="checklist roomy">
      <li>Deploys in minutes</li>
      <li>No domain merge or tenant migration required</li>
      <li>Works for both small groups and large distributed teams</li>
      <li>Ideal for temporary or long-term cross-tenant coexistence</li>
    </ul>
  </section>

  <footer class="cta-band">
    <div class="cta-button">REQUEST A 15-MINUTE DEMO</div>
  </footer>

</main>
</body>
</html>
```